New cool to-go cup for KELMO Coffee

UPDATE MARCH 18: Please read the attached document "Design ideas - Front" with a mock-up of the design we are looking for. And please don't change the logo.

We are looking for a new cool design for our to-go cups in kraft paper (same style as the attached photo).

The idea:

We have three different cups sizes: 6oz, 8oz and 12oz. We call them “Tiny-Lark” (6oz), “Mid-Wren” (8oz) and “Tall-heron” (12oz) (refers to the size in milliliters). We would like to include this in the cup design. Please see the attached sketch of the idea ("Design ideas - Front").

The backside of the cup should have the attached text and logo ("Design ideas - Back").

But other ideas are also very welcome too! Maybe just a simple cup with the logo.

Please keep the design very minimalistic. The more simple the better.

Target Market(s)

Young urban people

Industry/Entity Type

Coffee shop

Font styles to use
Sans Serif

Requirements
Must have
• Kraft paper cups

```html
<!DOCTYPE html>
<html lang="en">
<head>
<meta charset="utf-8">
<title>KELMO Coffee – cup sleeves</title>
<link rel="stylesheet" href="https://fonts.googleapis.com/css2?family=Open+Sans:wght@300;400;600;700&display=swap">
<style>
  :root {
    --backdrop: #efefed;
    --kraft: #a98a63;
    --kraft-light: #bd9f79;
    --ink: #4a2a18;
    --grain: #9a6f45;
    --engraving: #6e5238;
    --label-text: #f3e9dc;
  }
  * { box-sizing: border-box; margin: 0; padding: 0; }
  html, body { width: 1200px; height: 857px; overflow: hidden; }
  body {
    background: var(--backdrop);
    font-family: "Open Sans", Arial, sans-serif;
    color: var(--ink);
    display: flex;
    align-items: flex-end;
    justify-content: center;
    gap: 40px;
    padding-bottom: 150px;
  }
  .sleeve {
    position: relative;
    background: radial-gradient(ellipse at 50% 40%, var(--kraft-light), var(--kraft) 75%);
    clip-path: polygon(0 0, 100% 0, 91% 100%, 9% 100%);
    overflow: hidden;
    display: flex;
    flex-direction: column;
    align-items: center;
  }
  .sleeve--tiny { width: 300px; height: 300px; }
  .sleeve--mid { width: 340px; height: 350px; }
  .sleeve--tall { width: 380px; height: 400px; }
  .engraving {
    position: absolute;
    width: 34%;
    height: 60%;
    background: radial-gradient(ellipse at center, var(--engraving) 0%, rgba(110,82,56,0.35) 45%, rgba(110,82,56,0) 75%);
    opacity: 0.5;
  }
  .engraving--left { top: -4%; left: -6%; }
  .engraving--right { top: -4%; right: -6%; }
  .woodgrain {
    position: absolute;
    left: 0; right: 0; bottom: 0;
    height: 45%;
    background: linear-gradient(180deg, rgba(154,111,69,0) 0%, rgba(154,111,69,0.45) 60%, rgba(154,111,69,0.25) 100%);
  }
  .brand {
    position: relative;
    margin-top: 15%;
    width: 112px;
    height: 112px;
    border: 3px solid var(--ink);
    border-radius: 50%;
    display: flex;
    flex-direction: column;
    align-items: center;
    justify-content: center;
    font-weight: 600;
    font-size: 17px;
    line-height: 1.15;
    letter-spacing: 0.12em;
    text-align: center;
  }
  .sleeve--tall .brand { width: 124px; height: 124px; font-size: 19px; }
  .size-name {
    position: relative;
    margin-top: 14px;
    font-size: 32px;
    letter-spacing: -0.01em;
  }
  .size-name b { font-weight: 700; }
  .size-name span { font-weight: 300; }
  .info-label {
    position: absolute;
    bottom: 18px;
    left: 50%;
    transform: translateX(-50%);
    background: var(--ink);
    color: var(--label-text);
    border: 1px solid var(--label-text);
    outline: 2px solid var(--ink);
    padding: 5px 8px;
    font-size: 8px;
    line-height: 1.3;
    text-align: center;
    width: 150px;
  }
  .info-label strong { font-weight: 700; }
</style>
</head>
<body>
  <section class="sleeve sleeve--mid" aria-label="Mid-Wren sleeve">
    <div class="engraving engraving--left" role="img" aria-label="Engraved coffee branch illustration"></div>
    <div class="engraving engraving--right" role="img" aria-label="Engraved coffee branch illustration"></div>
    <div class="woodgrain" role="img" aria-label="Wood grain pattern"></div>
    <div class="brand">KELMO<br>Coffee</div>
    <p class="size-name"><b>Mid-</b><span>Wren</span></p>
    <p class="info-label">Read about your coffee<br>and the dedicated farmers<br>who made this cup possible.<br><strong>www.kelmo.com</strong><br>@kelmocoffee</p>
  </section>

  <section class="sleeve sleeve--tiny" aria-label="Tiny-Lark sleeve">
    <div class="engraving engraving--left" role="img" aria-label="Engraved coffee branch illustration"></div>
    <div class="engraving engraving--right" role="img" aria-label="Engraved coffee branch illustration"></div>
    <div class="woodgrain" role="img" aria-label="Wood grain pattern"></div>
    <div class="brand">KELMO<br>Coffee</div>
    <p class="size-name"><b>Tiny-</b><span>Lark</span></p>
    <p class="info-label">Read about your coffee<br>and the dedicated farmers<br>who made this cup possible.<br><strong>www.kelmo.com</strong><br>@kelmocoffee</p>
  </section>

  <section class="sleeve sleeve--tall" aria-label="Tall-heron sleeve">
    <div class="engraving engraving--left" role="img" aria-label="Engraved coffee branch illustration"></div>
    <div class="engraving engraving--right" role="img" aria-label="Engraved coffee branch illustration"></div>
    <div class="woodgrain" role="img" aria-label="Wood grain pattern"></div>
    <div class="brand">KELMO<br>Coffee</div>
    <p class="size-name"><b>Tall-</b><span>heron</span></p>
    <p class="info-label">Read about your coffee<br>and the dedicated farmers<br>who made this cup possible.<br><strong>www.kelmo.com</strong><br>@kelmocoffee</p>
  </section>
</body>
</html>
```